Design Android App for Creating Estimates and Invoices

This project is to create a graphic design for an Android mobile app called Velmira Builder App which is an app that will help contractors to quickly create professional estimates and invoices, accept payments, manage clients and projects and run their business smoothly.

Link to some designs I created myself, hoping to get even better design from you
https://snapvault.example/album/qTrWpe

This project is similar to
https://appmarket.example/store/apps/details?id=com.brevlo.android.brevlo
https://appmarket.example/store/apps/details?id=com.tuvrq.quikbill

Check this Google Doc for more information. http://shrtn.example/8KmPqX4

Target Market(s)

Contractors, Home Improvement Professionals, Home Builders,

Industry/Entity Type

Residential Construction

Requirements
Must have
• Non-cluttered screen for Estimates, Enough white space between fields.
Nice to have
• Be different from the two example designs shown

```html
<!DOCTYPE html>
<html lang="en">
<head>
<meta charset="utf-8">
<title>Velmira Builder App – Android App Design Concept</title>
<link href="https://fonts.googleapis.com/css2?family=Poppins:wght@300;400;500;600;700&display=swap" rel="stylesheet">
<style>
:root{
  --orange:#fd7a12;
  --orange-dim:#a9693a;
  --blue:#1f4f9f;
  --ink:#333;
  --muted:#9a9a9a;
  --faint:#c4c4c4;
  --line:#ececec;
  --backdrop:#ebe3de;
  --dim:#909090;
  --green:#6cc02a;
}
*{box-sizing:border-box;margin:0;padding:0}
html,body{width:1200px;height:652px;overflow:hidden;background:#fff}
body{font-family:"Poppins",sans-serif;color:var(--ink)}
.stage{position:absolute;left:0;top:0;width:2576px;height:1400px;transform:scale(.46584);transform-origin:0 0}
.intro{position:absolute;left:0;top:0;width:620px;height:1400px;background:#fff}
.showcase{position:absolute;left:620px;top:0;width:1956px;height:1400px;background:var(--backdrop)}
.abs{position:absolute}

/* hero screen */
.hero-screen{position:absolute;left:161px;top:228px;width:308px;height:615px;background:#fff;border-radius:10px;overflow:hidden;box-shadow:0 0 0 1px #e6e6e6}
.brand{position:absolute;left:120px;top:964px;display:flex;align-items:center;gap:30px}
.brand-dot{width:120px;height:120px;border-radius:50%;background:var(--orange)}
.brand-name{font-size:50px;font-weight:600;letter-spacing:12px;color:var(--blue)}
.tagline{position:absolute;left:0;width:636px;top:1108px;text-align:center;font-size:45px;font-weight:300;line-height:61px;color:#555}

/* phone screens */
.screen{position:absolute;width:264px;height:528px;background:#fff;overflow:hidden}
.screen.dim{background:var(--dim)}
.status{position:absolute;top:3px;right:6px;display:flex;align-items:center;gap:3px;font-size:7.5px;color:#b5b5b5}
.status.light{color:#fff}
.sysnav{position:absolute;left:0;right:0;bottom:0;height:30px}
.sysnav svg{position:absolute;top:10px}
.appbar-title{position:absolute;left:0;right:0;top:34px;text-align:center;font-size:11px;font-weight:500}
.back{position:absolute;left:14px;top:35px}
.track{position:absolute;left:0;right:0;top:56px;height:1px;background:var(--line)}
.progress{position:absolute;left:0;top:55px;height:3px;background:var(--orange)}
.dim .track{background:#888}
.btn{position:absolute;background:var(--orange);color:#fff;font-size:10px;font-weight:600;display:flex;align-items:center;justify-content:center;border-radius:2px}
.dim .btn.behind{background:var(--orange-dim);color:#d9c3b2}
.back-btn{position:absolute;left:15px;top:455px;width:40px;height:33px;border:1px solid var(--line);border-radius:2px;display:flex;align-items:center;justify-content:center;background:#fff}
.dim .back-btn{background:var(--dim);border-color:#888}
.field{position:absolute;border:1px solid #e4e4e4;border-radius:2px;font-size:6.5px;color:var(--faint);padding:0 6px;display:flex;align-items:center;background:#fff}
.field.tall{align-items:flex-start;padding-top:7px}
.link{position:absolute;left:0;right:0;text-align:center;font-size:8px;font-weight:500;color:var(--blue)}
.empty-msg{position:absolute;left:0;right:0;text-align:center;font-size:9px;font-weight:500}
.section{position:absolute;left:15px;font-size:9.5px;font-weight:500}
.label{position:absolute;left:15px;font-size:7px}
.value{position:absolute;right:15px;font-size:7px;color:var(--muted);text-align:right}
.modal{position:absolute;background:#fff;border-radius:2px}
.modal-title{position:absolute;left:0;right:0;text-align:center;font-size:9.5px;font-weight:500}
.mini-input{position:absolute;right:15px;width:50px;height:22px;border:1px solid #e8e8e8;border-radius:2px;font-size:6.5px;color:var(--faint);display:flex;align-items:center;justify-content:flex-end;padding-right:7px}
.check{position:absolute;right:15px;width:12px;height:12px}
.rule{position:absolute;left:15px;right:15px;height:1px;background:var(--line)}

/* estimates list */
.appbar-orange{position:absolute;left:0;right:0;top:0;height:68px;background:var(--orange)}
.appbar-orange h1{position:absolute;left:15px;top:34px;font-size:15.5px;font-weight:600;color:#fff}
.est-list{position:absolute;left:15px;right:15px;top:90px}
.est-row{height:40.5px;border-bottom:1px solid var(--line);display:flex;justify-content:space-between;align-items:center}
.est-title{font-size:7px;color:var(--ink)}
.est-ref{font-size:5.5px;color:var(--faint);margin-top:2px}
.est-meta{text-align:right}
.est-date{font-size:5.5px;color:var(--faint)}
.est-amt{font-size:7px;font-weight:500;margin-top:1px}
.hero-screen .appbar-orange{height:78px}
.hero-screen .appbar-orange h1{left:17px;top:38px;font-size:19px}
.hero-screen .est-list{left:17px;right:17px;top:92px}
.hero-screen .est-row{height:47.3px}
.hero-screen .est-title{font-size:9px}
.hero-screen .est-ref{font-size:6.5px}
.hero-screen .est-date{font-size:6.5px}
.hero-screen .est-amt{font-size:9.5px}
.fab{position:absolute;border-radius:50%;background:var(--orange);display:flex;align-items:center;justify-content:center;box-shadow:0 3px 6px rgba(253,122,18,.35)}
.tabbar{position:absolute;left:0;right:0;border-top:1px solid var(--line)}
.tab{position:absolute;text-align:center;color:#aaa}
.tab.active{color:var(--orange)}
.tab span{display:block;font-size:5px;margin-top:2px}
.hero-screen .tab span{font-size:6px}

/* clients */
.client{position:absolute;left:16px;right:15px;height:50px;border:1px solid var(--line);border-radius:2px}
.client.selected{border-color:var(--blue)}
.avatar{position:absolute;left:10px;top:7px;width:36px;height:36px;border-radius:50%;background:var(--green);color:#fff;font-size:14px;font-weight:600;display:flex;align-items:center;justify-content:center}
.client-name{position:absolute;left:58px;top:9px;font-size:7px}
.client-info{position:absolute;left:58px;top:19px;font-size:5px;color:var(--muted);line-height:8px}
.item-row .label{font-size:7.5px}
.sub{position:absolute;left:15px;font-size:5px;color:var(--muted)}
</style>
</head>
<body>
<div class="stage">

  <section class="intro">
    <div class="hero-screen">
      <div class="appbar-orange">
        <div class="status light" style="top:3px;font-size:9px">
          <svg width="10" height="8" viewBox="0 0 10 8"><path d="M0 0h10L5 8z" fill="#fff"/></svg>
          <svg width="8" height="8" viewBox="0 0 8 8"><path d="M8 0v8H0z" fill="#fff"/></svg>
          <svg width="5" height="9" viewBox="0 0 5 9"><rect width="5" height="9" fill="#fff"/></svg>12:30
        </div>
        <h1>Estimates</h1>
        <svg class="abs" style="left:272px;top:43px" width="17" height="17" viewBox="0 0 17 17"><circle cx="7" cy="7" r="5.5" fill="none" stroke="#fff" stroke-width="1.6"/><path d="M11 11l4.5 4.5" stroke="#fff" stroke-width="1.6"/></svg>
      </div>
      <div class="est-list">
        <div class="est-row"><div><p class="est-title">EST0021 - Harlow Builders</p><p class="est-ref">93930283</p></div><div class="est-meta"><p class="est-date">May 6, 2019</p><p class="est-amt">$2512.50</p></div></div>
        <div class="est-row"><div><p class="est-title">EST0022 - Crestline Inc.</p><p class="est-ref">34230283</p></div><div class="est-meta"><p class="est-date">May 6, 2019</p><p class="est-amt">$1106.00</p></div></div>
        <div class="est-row"><div><p class="est-title">EST0026 - Obi and Sons LTD.</p><p class="est-ref">19330283</p></div><div class="est-meta"><p class="est-date">May 8, 2019</p><p class="est-amt">$4500.00</p></div></div>
        <div class="est-row"><div><p class="est-title">EST0031 - Harlow Builders</p><p class="est-ref">93930283</p></div><div class="est-meta"><p class="est-date">May 6, 2019</p><p class="est-amt">$2512.50</p></div></div>
        <div class="est-row"><div><p class="est-title">EST0045 - Crestline Inc.</p><p class="est-ref">34230283</p></div><div class="est-meta"><p class="est-date">May 6, 2019</p><p class="est-amt">$1106.00</p></div></div>
        <div class="est-row"><div><p class="est-title">EST0068 - Obi and Sons LTD.</p><p class="est-ref">19330283</p></div><div class="est-meta"><p class="est-date">May 8, 2019</p><p class="est-amt">$4500.00</p></div></div>
      </div>
      <div class="fab" style="left:249px;top:493px;width:42px;height:42px"><svg width="14" height="14" viewBox="0 0 14 14"><path d="M7 1v12M1 7h12" stroke="#fff" stroke-width="1.8"/></svg></div>
      <div class="tabbar" style="top:550px;height:65px">
        <div class="tab active" style="left:30px;top:16px;width:40px"><svg width="18" height="18" viewBox="0 0 18 18"><circle cx="9" cy="9" r="7" fill="none" stroke="currentColor"/><path d="M9 2v7h7" fill="none" stroke="currentColor"/></svg><span>Estimates</span></div>
        <div class="tab" style="left:99px;top:16px;width:40px"><svg width="18" height="18" viewBox="0 0 18 18"><rect x="4" y="1.5" width="10" height="15" fill="none" stroke="currentColor"/><path d="M6 6h6M6 9h6M6 12h4" stroke="currentColor"/></svg><span>Invoices</span></div>
        <div class="tab" style="left:168px;top:16px;width:40px"><svg width="18" height="18" viewBox="0 0 18 18"><circle cx="7" cy="6" r="3" fill="none" stroke="currentColor"/><circle cx="12" cy="6" r="3" fill="none" stroke="currentColor"/><path d="M2 17v-4a5 5 0 0 1 10 0v4M12 11a4 4 0 0 1 4 4v2" fill="none" stroke="currentColor"/></svg><span>Clients</span></div>
        <div class="tab" style="left:237px;top:16px;width:40px"><svg width="18" height="18" viewBox="0 0 18 18"><circle cx="9" cy="9" r="7.5" fill="none" stroke="currentColor"/><circle cx="9" cy="9" r="4.5" fill="none" stroke="currentColor"/><circle cx="9" cy="9" r="1.6" fill="none" stroke="currentColor"/></svg><span>Settings</span></div>
      </div>
    </div>

    <div class="brand"><span class="brand-dot"></span><span class="brand-name">VELMIRA</span></div>
    <p class="tagline">Android App Design<br>Concept</p>
  </section>

  <section class="showcase">

    <!-- Sign in -->
    <div class="screen" style="left:45px;top:152px">
      <div class="status"><svg width="8" height="6" viewBox="0 0 8 6"><path d="M0 0h8L4 6z" fill="#c4c4c4"/></svg><svg width="6" height="6" viewBox="0 0 6 6"><path d="M6 0v6H0z" fill="#c4c4c4"/></svg><svg width="4" height="7" viewBox="0 0 4 7"><rect width="4" height="7" fill="#c4c4c4"/></svg>12:30</div>
      <div class="abs" style="left:111px;top:80px;width:42px;height:42px;border-radius:50%;background:var(--orange)"></div>
      <p class="abs" style="left:0;right:0;top:134px;text-align:center;font-size:16px;font-weight:600;letter-spacing:4px;color:var(--blue)">VELMIRA</p>
      <div class="field" style="left:15px;top:176px;width:233px;height:30px">Work Email</div>
      <div class="field" style="left:15px;top:217px;width:233px;height:30px">Password</div>
      <p class="abs" style="right:16px;top:254px;font-size:7px;font-weight:500;color:var(--blue)">Forgot Password?</p>
      <div class="btn" style="left:15px;top:282px;width:233px;height:33px">Sign In</div>
      <p class="abs" style="left:0;right:0;top:335px;text-align:center;font-size:7px">Don't have an account? <b style="color:var(--blue);font-weight:500">Sign Up</b></p>
      <p class="abs" style="left:12px;right:12px;top:463px;text-align:center;font-size:6.5px;line-height:12px;color:#666">By clicking Sign In, you are indicating that you have read and agreed to the <b style="color:var(--blue);font-weight:500">Privacy Policy</b> and <b style="color:var(--blue);font-weight:500">Terms of Service</b></p>
      <div class="sysnav"><svg style="left:50px" width="7" height="8" viewBox="0 0 7 8"><path d="M7 0v8L0 4z" fill="#bbb"/></svg><svg style="left:127px" width="9" height="9" viewBox="0 0 9 9"><circle cx="4.5" cy="4.5" r="4.5" fill="#bbb"/></svg><svg style="left:210px" width="7" height="7" viewBox="0 0 7 7"><rect width="7" height="7" fill="#bbb"/></svg></div>
    </div>

    <!-- Estimates list -->
    <div class="screen" style="left:345px;top:152px">
      <div class="appbar-orange">
        <div class="status light"><svg width="8" height="6" viewBox="0 0 8 6"><path d="M0 0h8L4 6z" fill="#fff"/></svg><svg width="6" height="6" viewBox="0 0 6 6"><path d="M6 0v6H0z" fill="#fff"/></svg><svg width="4" height="7" viewBox="0 0 4 7"><rect width="4" height="7" fill="#fff"/></svg>12:30</div>
        <h1>Estimates</h1>
        <svg class="abs" style="left:234px;top:38px" width="14" height="14" viewBox="0 0 17 17"><circle cx="7" cy="7" r="5.5" fill="none" stroke="#fff" stroke-width="1.6"/><path d="M11 11l4.5 4.5" stroke="#fff" stroke-width="1.6"/></svg>
      </div>
      <div class="est-list">
        <div class="est-row"><div><p class="est-title">EST0021 - Harlow Builders</p><p class="est-ref">93930283</p></div><div class="est-meta"><p class="est-date">May 6, 2019</p><p class="est-amt">$2512.50</p></div></div>
        <div class="est-row"><div><p class="est-title">EST0022 - Crestline Inc.</p><p class="est-ref">34230283</p></div><div class="est-meta"><p class="est-date">May 6, 2019</p><p class="est-amt">$1106.00</p></div></div>
        <div class="est-row"><div><p class="est-title">EST0026 - Obi and Sons LTD.</p><p class="est-ref">19330283</p></div><div class="est-meta"><p class="est-date">May 8, 2019</p><p class="est-amt">$4500.00</p></div></div>
        <div class="est-row"><div><p class="est-title">EST0031 - Harlow Builders</p><p class="est-ref">93930283</p></div><div class="est-meta"><p class="est-date">May 6, 2019</p><p class="est-amt">$2512.50</p></div></div>
        <div class="est-row"><div><p class="est-title">EST0045 - Crestline Inc.</p><p class="est-ref">34230283</p></div><div class="est-meta"><p class="est-date">May 6, 2019</p><p class="est-amt">$1106.00</p></div></div>
        <div class="est-row"><div><p class="est-title">EST0068 - Obi and Sons LTD.</p><p class="est-ref">19330283</p></div><div class="est-meta"><p class="est-date">May 8, 2019</p><p class="est-amt">$4500.00</p></div></div>
      </div>
      <div class="fab" style="left:213px;top:423px;width:36px;height:36px"><svg width="12" height="12" viewBox="0 0 14 14"><path d="M7 1v12M1 7h12" stroke="#fff" stroke-width="1.8"/></svg></div>
      <div class="tabbar" style="top:472px;height:28px">
        <div class="tab active" style="left:29px;top:10px;width:30px"><svg width="14" height="14" viewBox="0 0 18 18"><circle cx="9" cy="9" r="7" fill="none" stroke="currentColor"/><path d="M9 2v7h7" fill="none" stroke="currentColor"/></svg><span>Estimates</span></div>
        <div class="tab" style="left:88px;top:10px;width:30px"><svg width="14" height="14" viewBox="0 0 18 18"><rect x="4" y="1.5" width="10" height="15" fill="none" stroke="currentColor"/><path d="M6 6h6M6 9h6M6 12h4" stroke="currentColor"/></svg><span>Invoices</span></div>
        <div class="tab" style="left:146px;top:10px;width:30px"><svg width="14" height="14" viewBox="0 0 18 18"><circle cx="7" cy="6" r="3" fill="none" stroke="currentColor"/><circle cx="12" cy="6" r="3" fill="none" stroke="currentColor"/><path d="M2 17v-4a5 5 0 0 1 10 0v4M12 11a4 4 0 0 1 4 4v2" fill="none" stroke="currentColor"/></svg><span>Clients</span></div>
        <div class="tab" style="left:205px;top:10px;width:30px"><svg width="14" height="14" viewBox="0 0 18 18"><circle cx="9" cy="9" r="7.5" fill="none" stroke="currentColor"/><circle cx="9" cy="9" r="4.5" fill="none" stroke="currentColor"/><circle cx="9" cy="9" r="1.6" fill="none" stroke="currentColor"/></svg><span>Settings</span></div>
      </div>
      <div class="sysnav"><svg style="left:50px" width="7" height="8" viewBox="0 0 7 8"><path d="M7 0v8L0 4z" fill="#bbb"/></svg><svg style="left:127px" width="9" height="9" viewBox="0 0 9 9"><circle cx="4.5" cy="4.5" r="4.5" fill="#bbb"/></svg><svg style="left:210px" width="7" height="7" viewBox="0 0 7 7"><rect width="7" height="7" fill="#bbb"/></svg></div>
    </div>

    <!-- No clients -->
    <div class="screen" style="left:646px;top:152px">
      <div class="status"><svg width="8" height="6" viewBox="0 0 8 6"><path d="M0 0h8L4 6z" fill="#c4c4c4"/></svg><svg width="6" height="6" viewBox="0 0 6 6"><path d="M6 0v6H0z" fill="#c4c4c4"/></svg><svg width="4" height="7" viewBox="0 0 4 7"><rect width="4" height="7" fill="#c4c4c4"/></svg>12:30</div>
      <svg class="back" width="8" height="10" viewBox="0 0 8 10"><path d="M6 1L2 5l4 4" fill="none" stroke="#333" stroke-width="1.3"/></svg>
      <p class="appbar-title">New Estimate</p>
      <div class="track"></div><div class="progress" style="width:65px"></div>
      <svg class="abs" style="left:108px;top:138px" width="48" height="70" viewBox="0 0 48 70"><circle cx="24" cy="24" r="22" fill="none" stroke="#333" stroke-width="2"/><circle cx="24" cy="19" r="8" fill="none" stroke="#333" stroke-width="2"/><path d="M10 40a15 14 0 0 1 28 0" fill="none" stroke="#333" stroke-width="2"/><path d="M8 56h32M14 64h20" stroke="var(--blue)" stroke-width="2"/></svg>
      <p class="empty-msg" style="top:223px">You haven't added any clients yet</p>
      <p class="link" style="top:250px">+ Add Client</p>
      <div class="btn" style="left:15px;top:455px;width:234px;height:33px">Next</div>
      <div class="sysnav"><svg style="left:50px" width="7" height="8" viewBox="0 0 7 8"><path d="M7 0v8L0 4z" fill="#bbb"/></svg><svg style="left:127px" width="9" height="9" viewBox="0 0 9 9"><circle cx="4.5" cy="4.5" r="4.5" fill="#bbb"/></svg><svg style="left:210px" width="7" height="7" viewBox="0 0 7 7"><rect width="7" height="7" fill="#bbb"/></svg></div>
    </div>

    <!-- Add client modal -->
    <div class="screen dim" style="left:946px;top:152px">
      <div class="status"><svg width="8" height="6" viewBox="0 0 8 6"><path d="M0 0h8L4 6z" fill="#a8a8a8"/></svg><svg width="6" height="6" viewBox="0 0 6 6"><path d="M6 0v6H0z" fill="#a8a8a8"/></svg><svg width="4" height="7" viewBox="0 0 4 7"><rect width="4" height="7" fill="#a8a8a8"/></svg>12:30</div>
      <svg class="back" width="8" height="10" viewBox="0 0 8 10"><path d="M6 1L2 5l4 4" fill="none" stroke="#333" stroke-width="1.3"/></svg>
      <p class="appbar-title">New Estimate</p>
      <div class="track"></div><div class="progress" style="width:65px;background:var(--orange-dim)"></div>
      <div class="modal" style="left:16px;top:64px;width:233px;height:392px">
        <p class="modal-title" style="top:16px">Add Client</p>
        <p class="abs" style="left:13px;top:44px;font-size:6.5px;font-weight:500">Basic Information</p>
        <div class="field" style="left:14px;top:58px;width:205px;height:24px">Fullname</div>
        <div class="field" style="left:14px;top:90px;width:205px;height:24px">Email Address</div>
        <div class="field" style="left:14px;top:121px;width:205px;height:24px">Phone Number</div>
        <div class="field" style="left:14px;top:153px;width:205px;height:24px">Company Name</div>
        <p class="abs" style="left:13px;top:192px;font-size:6.5px;font-weight:500">Billing Address</p>
        <div class="field" style="left:14px;top:206px;width:205px;height:24px">Address</div>
        <div class="field" style="left:14px;top:237px;width:205px;height:24px">City</div>
        <div class="field" style="left:14px;top:269px;width:205px;height:24px">State or Province</div>
        <div class="field" style="left:14px;top:300px;width:205px;height:24px">Zip or Postal Code</div>
        <div class="btn" style="left:16px;top:348px;width:203px;height:31px">Save Client</div>
      </div>
      <div class="btn behind" style="left:15px;top:456px;width:234px;height:32px">Next</div>
      <div class="sysnav"><svg style="left:50px" width="7" height="8" viewBox="0 0 7 8"><path d="M7 0v8L0 4z" fill="#777"/></svg><svg style="left:127px" width="9" height="9" viewBox="0 0 9 9"><circle cx="4.5" cy="4.5" r="4.5" fill="#777"/></svg><svg style="left:210px" width="7" height="7" viewBox="0 0 7 7"><rect width="7" height="7" fill="#777"/></svg></div>
    </div>

    <!-- Client list -->
    <div class="screen" style="left:1247px;top:152px">
      <div class="status"><svg width="8" height="6" viewBox="0 0 8 6"><path d="M0 0h8L4 6z" fill="#c4c4c4"/></svg><svg width="6" height="6" viewBox="0 0 6 6"><path d="M6 0v6H0z" fill="#c4c4c4"/></svg><svg width="4" height="7" viewBox="0 0 4 7"><rect width="4" height="7" fill="#c4c4c4"/></svg>12:30</div>
      <svg class="back" width="8" height="10" viewBox="0 0 8 10"><path d="M6 1L2 5l4 4" fill="none" stroke="#333" stroke-width="1.3"/></svg>
      <p class="appbar-title">New Estimate</p>
      <div class="track"></div><div class="progress" style="width:65px"></div>
      <p class="section" style="top:86px">Clients</p>
      <div class="client selected" style="top:106px">
        <div class="avatar">TE</div>
        <p class="client-name">Tobenna Eze</p>
        <p class="client-info">tobenna.e@mailbox.example<br>Dalton, TX</p>
        <svg class="abs" style="right:9px;top:7px" width="12" height="12" viewBox="0 0 12 12"><circle cx="6" cy="6" r="5.4" fill="none" stroke="var(--blue)" stroke-width=".8"/><path d="M3.5 6.2l1.7 1.6 3.3-3.4" fill="none" stroke="var(--blue)" stroke-width=".9"/></svg>
      </div>
      <div class="client" style="top:170px">
        <div class="avatar">MR</div>
        <p class="client-name">Marcus Reed</p>
        <p class="client-info">marcusreed@mailbox.example<br>Enugu, NG</p>
        <svg class="abs" style="right:9px;top:7px" width="12" height="12" viewBox="0 0 12 12"><circle cx="6" cy="6" r="5.4" fill="none" stroke="#e4e4e4" stroke-width=".8"/></svg>
      </div>
      <p class="link" style="top:235px;font-size:7px">+ Add Client</p>
      <div class="btn" style="left:15px;top:455px;width:234px;height:33px">Next</div>
      <div class="sysnav"><svg style="left:50px" width="7" height="8" viewBox="0 0 7 8"><path d="M7 0v8L0 4z" fill="#bbb"/></svg><svg style="left:127px" width="9" height="9" viewBox="0 0 9 9"><circle cx="4.5" cy="4.5" r="4.5" fill="#bbb"/></svg><svg style="left:210px" width="7" height="7" viewBox="0 0 7 7"><rect width="7" height="7" fill="#bbb"/></svg></div>
    </div>

    <!-- No items -->
    <div class="screen" style="left:1548px;top:152px">
      <div class="status"><svg width="8" height="6" viewBox="0 0 8 6"><path d="M0 0h8L4 6z" fill="#c4c4c4"/></svg><svg width="6" height="6" viewBox="0 0 6 6"><path d="M6 0v6H0z" fill="#c4c4c4"/></svg><svg width="4" height="7" viewBox="0 0 4 7"><rect width="4" height="7" fill="#c4c4c4"/></svg>12:30</div>
      <svg class="back" width="8" height="10" viewBox="0 0 8 10"><path d="M6 1L2 5l4 4" fill="none" stroke="#333" stroke-width="1.3"/></svg>
      <p class="appbar-title">New Estimate</p>
      <div class="track"></div><div class="progress" style="width:113px"></div>
      <svg class="abs" style="left:102px;top:137px" width="62" height="56" viewBox="0 0 62 56"><circle cx="8" cy="8" r="6" fill="none" stroke="#333" stroke-width="2"/><circle cx="8" cy="28" r="6" fill="none" stroke="var(--blue)" stroke-width="2"/><circle cx="8" cy="48" r="6" fill="none" stroke="#333" stroke-width="2"/><path d="M22 8h38M22 28h38M22 48h38" stroke="#333" stroke-width="2"/><path d="M22 28h38" stroke="var(--blue)" stroke-width="2"/></svg>
      <p class="empty-msg" style="top:208px">There are no items on your list</p>
      <p class="link" style="top:235px">+ Add Item</p>
      <div class="back-btn"><svg width="10" height="8" viewBox="0 0 10 8"><path d="M4 1L1 4l3 3M1 4h9" fill="none" stroke="#999"/></svg></div>
      <div class="btn" style="left:63px;top:455px;width:186px;height:33px">Next</div>
      <div class="sysnav"><svg style="left:50px" width="7" height="8" viewBox="0 0 7 8"><path d="M7 0v8L0 4z" fill="#bbb"/></svg><svg style="left:127px" width="9" height="9" viewBox="0 0 9 9"><circle cx="4.5" cy="4.5" r="4.5" fill="#bbb"/></svg><svg style="left:210px" width="7" height="7" viewBox="0 0 7 7"><rect width="7" height="7" fill="#bbb"/></svg></div>
    </div>

    <!-- Add item modal -->
    <div class="screen dim" style="left:345px;top:720px">
      <div class="status"><svg width="8" height="6" viewBox="0 0 8 6"><path d="M0 0h8L4 6z" fill="#a8a8a8"/></svg><svg width="6" height="6" viewBox="0 0 6 6"><path d="M6 0v6H0z" fill="#a8a8a8"/></svg><svg width="4" height="7" viewBox="0 0 4 7"><rect width="4" height="7" fill="#a8a8a8"/></svg>12:30</div>
      <svg class="back" width="8" height="10" viewBox="0 0 8 10"><path d="M6 1L2 5l4 4" fill="none" stroke="#333" stroke-width="1.3"/></svg>
      <p class="appbar-title">New Estimate</p>
      <div class="track"></div><div class="progress" style="width:112px;background:var(--orange-dim)"></div>
      <div class="modal" style="left:16px;top:104px;width:233px;height:312px">
        <p class="modal-title" style="top:15px">Add Item</p>
        <div class="field" style="left:14px;top:42px;width:205px;height:25px">Item Name</div>
        <div class="field tall" style="left:14px;top:74px;width:205px;height:50px">Item Description</div>
        <p class="abs" style="left:12px;top:139px;font-size:7px;font-weight:500">Unit Cost</p>
        <div class="mini-input" style="right:14px;top:132px;width:50px">$0.00</div>
        <p class="abs" style="left:12px;top:171px;font-size:7px;font-weight:500">Quantity</p>
        <div class="mini-input" style="right:14px;top:164px">0</div>
        <p class="abs" style="left:12px;top:202px;font-size:7px;font-weight:500">Tax</p>
        <div class="mini-input" style="right:14px;top:195px">0%</div>
        <p class="abs" style="left:12px;top:234px;font-size:7px;font-weight:500">Total Cost</p>
        <p class="abs" style="right:14px;top:234px;font-size:7px;font-weight:500;color:var(--blue)">$0.00</p>
        <div class="btn" style="left:14px;top:268px;width:206px;height:31px">Save Item</div>
      </div>
      <div class="back-btn"><svg width="10" height="8" viewBox="0 0 10 8"><path d="M4 1L1 4l3 3M1 4h9" fill="none" stroke="#777"/></svg></div>
      <div class="btn behind" style="left:63px;top:455px;width:186px;height:33px">Next</div>
      <div class="sysnav"><svg style="left:50px" width="7" height="8" viewBox="0 0 7 8"><path d="M7 0v8L0 4z" fill="#777"/></svg><svg style="left:127px" width="9" height="9" viewBox="0 0 9 9"><circle cx="4.5" cy="4.5" r="4.5" fill="#777"/></svg><svg style="left:210px" width="7" height="7" viewBox="0 0 7 7"><rect width="7" height="7" fill="#777"/></svg></div>
    </div>

    <!-- Items summary -->
    <div class="screen" style="left:646px;top:720px">
      <div class="status"><svg width="8" height="6" viewBox="0 0 8 6"><path d="M0 0h8L4 6z" fill="#c4c4c4"/></svg><svg width="6" height="6" viewBox="0 0 6 6"><path d="M6 0v6H0z" fill="#c4c4c4"/></svg><svg width="4" height="7" viewBox="0 0 4 7"><rect width="4" height="7" fill="#c4c4c4"/></svg>12:30</div>
      <svg class="back" width="8" height="10" viewBox="0 0 8 10"><path d="M6 1L2 5l4 4" fill="none" stroke="#333" stroke-width="1.3"/></svg>
      <p class="appbar-title">New Estimate</p>
      <div class="track"></div><div class="progress" style="width:113px"></div>
      <p class="section" style="top:86px">Items</p>
      <p class="label" style="top:106px">Asphalt (per sq ft.)</p><p class="sub" style="top:117px">Inclusive of labour costs</p>
      <p class="value" style="top:106px;font-size:5px">12 x $100.00</p><p class="value" style="top:115px;color:var(--ink);font-weight:500">$1200.00</p>
      <div class="rule" style="top:133px"></div>
      <p class="label" style="top:143px">Tree and stump removal</p><p class="sub" style="top:154px">Inclusive of equipment rentals costs</p>
      <p class="value" style="top:143px;font-size:5px">4 x $62.50</p><p class="value" style="top:152px;color:var(--ink);font-weight:500">$250.00</p>
      <div class="rule" style="top:170px"></div>
      <p class="label" style="top:180px">Site cleanup (per hour)</p><p class="sub" style="top:191px">Preparing area for paving</p>
      <p class="value" style="top:180px;font-size:5px">8 x $70.00</p><p class="value" style="top:189px;color:var(--ink);font-weight:500">$560.00</p>
      <div class="rule" style="top:207px"></div>
      <p class="abs" style="left:15px;top:216px;font-size:6.5px;font-weight:500;color:var(--blue)">+ Add Item</p>
      <p class="label" style="top:245px;font-weight:500">Subtotal</p><p class="value" style="top:245px">$2,010.00</p>
      <p class="label" style="top:271px;font-weight:500">Markup</p><div class="mini-input" style="top:264px;width:56px">0</div>
      <p class="label" style="top:303px;font-weight:500">Discount</p><div class="mini-input" style="top:296px;width:56px">0%</div>
      <p class="label" style="top:334px;font-weight:500">Tax</p><p class="value" style="top:334px">$502.50</p>
      <div class="rule" style="top:352px"></div>
      <p class="abs" style="left:15px;top:370px;font-size:9.5px;font-weight:500">TOTAL</p>
      <p class="abs" style="right:15px;top:369px;font-size:10px;font-weight:600;color:var(--blue)">$2,512.50</p>
      <div class="back-btn"><svg width="10" height="8" viewBox="0 0 10 8"><path d="M4 1L1 4l3 3M1 4h9" fill="none" stroke="#999"/></svg></div>
      <div class="btn" style="left:63px;top:455px;width:186px;height:33px">Next</div>
      <div class="sysnav"><svg style="left:50px" width="7" height="8" viewBox="0 0 7 8"><path d="M7 0v8L0 4z" fill="#bbb"/></svg><svg style="left:127px" width="9" height="9" viewBox="0 0 9 9"><circle cx="4.5" cy="4.5" r="4.5" fill="#bbb"/></svg><svg style="left:210px" width="7" height="7" viewBox="0 0 7 7"><rect width="7" height="7" fill="#bbb"/></svg></div>
    </div>

    <!-- Payment options -->
    <div class="screen" style="left:946px;top:720px">
      <div class="status"><svg width="8" height="6" viewBox="0 0 8 6"><path d="M0 0h8L4 6z" fill="#c4c4c4"/></svg><svg width="6" height="6" viewBox="0 0 6 6"><path d="M6 0v6H0z" fill="#c4c4c4"/></svg><svg width="4" height="7" viewBox="0 0 4 7"><rect width="4" height="7" fill="#c4c4c4"/></svg>12:30</div>
      <svg class="back" width="8" height="10" viewBox="0 0 8 10"><path d="M6 1L2 5l4 4" fill="none" stroke="#333" stroke-width="1.3"/></svg>
      <p class="appbar-title">New Estimate</p>
      <div class="track"></div><div class="progress" style="width:172px"></div>
      <p class="section" style="top:86px">Payment Options</p>
      <p class="label" style="top:113px">Request Deposit</p>
      <div class="mini-input" style="top:106px;width:56px;justify-content:space-between;padding-left:10px">20%<svg width="6" height="4" viewBox="0 0 6 4"><path d="M.5.5L3 3 5.5.5" fill="none" stroke="#999"/></svg></div>
      <p class="label" style="top:147px">Payment Schedule</p><p class="value" style="top:147px;color:var(--blue);font-weight:500">Add</p>
      <p class="label" style="top:176px">Accept Credit Cards</p>
      <svg class="check" style="top:175px" viewBox="0 0 12 12"><circle cx="6" cy="6" r="5.4" fill="none" stroke="var(--blue)" stroke-width=".8"/><path d="M3.5 6.2l1.7 1.6 3.3-3.4" fill="none" stroke="var(--blue)" stroke-width=".9"/></svg>
      <p class="label" style="top:206px">Accept E-Check</p>
      <svg class="check" style="top:205px" viewBox="0 0 12 12"><circle cx="6" cy="6" r="5.4" fill="none" stroke="#e4e4e4" stroke-width=".8"/></svg>
      <p class="label" style="top:236px">Show Financing Options</p>
      <svg class="check" style="top:235px" viewBox="0 0 12 12"><circle cx="6" cy="6" r="5.4" fill="none" stroke="var(--blue)" stroke-width=".8"/><path d="M3.5 6.2l1.7 1.6 3.3-3.4" fill="none" stroke="var(--blue)" stroke-width=".9"/></svg>
      <p class="label" style="top:265px;font-weight:500">Client Note</p>
      <div class="field tall" style="left:15px;top:281px;width:234px;height:49px">Type your note here</div>
      <div class="back-btn"><svg width="10" height="8" viewBox="0 0 10 8"><path d="M4 1L1 4l3 3M1 4h9" fill="none" stroke="#999"/></svg></div>
      <div class="btn" style="left:63px;top:455px;width:186px;height:33px">Next</div>
      <div class="sysnav"><svg style="left:50px" width="7" height="8" viewBox="0 0 7 8"><path d="M7 0v8L0 4z" fill="#bbb"/></svg><svg style="left:127px" width="9" height="9" viewBox="0 0 9 9"><circle cx="4.5" cy="4.5" r="4.5" fill="#bbb"/></svg><svg style="left:210px" width="7" height="7" viewBox="0 0 7 7"><rect width="7" height="7" fill="#bbb"/></svg></div>
    </div>

    <!-- Upload photo -->
    <div class="screen" style="left:1247px;top:720px">
      <div class="status"><svg width="8" height="6" viewBox="0 0 8 6"><path d="M0 0h8L4 6z" fill="#c4c4c4"/></svg><svg width="6" height="6" viewBox="0 0 6 6"><path d="M6 0v6H0z" fill="#c4c4c4"/></svg><svg width="4" height="7" viewBox="0 0 4 7"><rect width="4" height="7" fill="#c4c4c4"/></svg>12:30</div>
      <svg class="back" width="8" height="10" viewBox="0 0 8 10"><path d="M6 1L2 5l4 4" fill="none" stroke="#333" stroke-width="1.3"/></svg>
      <p class="appbar-title">New Estimate</p>
      <div class="track"></div><div class="progress" style="width:208px"></div>
      <svg class="abs" style="left:106px;top:138px" width="52" height="56" viewBox="0 0 52 56"><path d="M26 46V3M14 15L26 3l12 12" fill="none" stroke="var(--blue)" stroke-width="2"/><path d="M2 42v12h48V42" fill="none" stroke="#333" stroke-width="2"/></svg>
      <p class="empty-msg" style="top:208px">Please upload a photo</p>
      <p class="link" style="top:235px">Upload Photo</p>
      <div class="back-btn"><svg width="10" height="8" viewBox="0 0 10 8"><path d="M4 1L1 4l3 3M1 4h9" fill="none" stroke="#999"/></svg></div>
      <div class="btn" style="left:63px;top:455px;width:186px;height:33px">Next</div>
      <div class="sysnav"><svg style="left:50px" width="7" height="8" viewBox="0 0 7 8"><path d="M7 0v8L0 4z" fill="#bbb"/></svg><svg style="left:127px" width="9" height="9" viewBox="0 0 9 9"><circle cx="4.5" cy="4.5" r="4.5" fill="#bbb"/></svg><svg style="left:210px" width="7" height="7" viewBox="0 0 7 7"><rect width="7" height="7" fill="#bbb"/></svg></div>
    </div>

    <!-- Signature & document info -->
    <div class="screen" style="left:1548px;top:720px">
      <div class="status"><svg width="8" height="6" viewBox="0 0 8 6"><path d="M0 0h8L4 6z" fill="#c4c4c4"/></svg><svg width="6" height="6" viewBox="0 0 6 6"><path d="M6 0v6H0z" fill="#c4c4c4"/></svg><svg width="4" height="7" viewBox="0 0 4 7"><rect width="4" height="7" fill="#c4c4c4"/></svg>12:30</div>
      <svg class="back" width="8" height="10" viewBox="0 0 8 10"><path d="M6 1L2 5l4 4" fill="none" stroke="#333" stroke-width="1.3"/></svg>
      <p class="appbar-title">New Estimate</p>
      <div class="track"></div><div class="progress" style="width:264px"></div>
      <p class="section" style="top:86px">Signature Options</p>
      <p class="label" style="top:108px">Client Signature</p>
      <svg class="check" style="top:106px" viewBox="0 0 12 12"><circle cx="6" cy="6" r="5.4" fill="none" stroke="var(--blue)" stroke-width=".8"/><path d="M3.5 6.2l1.7 1.6 3.3-3.4" fill="none" stroke="var(--blue)" stroke-width=".9"/></svg>
      <p class="label" style="top:138px">Company signature</p>
      <svg class="check" style="top:136px" viewBox="0 0 12 12"><circle cx="6" cy="6" r="5.4" fill="none" stroke="var(--blue)" stroke-width=".8"/><path d="M3.5 6.2l1.7 1.6 3.3-3.4" fill="none" stroke="var(--blue)" stroke-width=".9"/></svg>
      <p class="section" style="top:177px">Document Information</p>
      <p class="label" style="top:198px">Estimate ID</p><p class="value" style="top:198px">EST0021</p>
      <p class="label" style="top:226px">Date</p><p class="value" style="top:226px">Monday, May 6, 2019</p>
      <p class="label" style="top:254px">PO Number</p><p class="value" style="top:254px">93930283</p>
      <div class="btn" style="left:15px;top:455px;width:234px;height:33px">Save Estimate</div>
      <div class="sysnav"><svg style="left:50px" width="7" height="8" viewBox="0 0 7 8"><path d="M7 0v8L0 4z" fill="#bbb"/></svg><svg style="left:127px" width="9" height="9" viewBox="0 0 9 9"><circle cx="4.5" cy="4.5" r="4.5" fill="#bbb"/></svg><svg style="left:210px" width="7" height="7" viewBox="0 0 7 7"><rect width="7" height="7" fill="#bbb"/></svg></div>
    </div>

  </section>
</div>
</body>
</html>
```